REEL HARBOR PRODUCTION SERVICES needs a Brochure Design

We are a new company based in dubai that specializes in creative media production. We create conceptual tv commercials, corporate videos, music videos, documentaries, short films, training videos, time-lapses, we also cover live events and do photography.
We would like the designer to be creative in their design and also provide text to go with.
Link to our logo: http://www.artpitchhub.com/design/482031/logo-design-by-vantor-estudios
We want six pages:
1- Logo with web link at bottom of page
2- About Us
3- Services Offered
4- Equipment List
5- Equipment List continued
6- Contact Us
PS: Use champagne & limousines Font.
Our Address:
Blgd. Al Nakheel Tower, Off. 204, Al Safwa
Dubai, UAE
T: +9714 521 7093
PoBox. 38215
Web: www.reelharbordubai.com
Please do not copy or create exactly the same "About Us" that is found in the attached files. We are looking for something more professional along the same lines.

```html
<!DOCTYPE html>
<html lang="en">
<head>
<meta charset="utf-8">
<title>Reel Harbor Production Services – Brochure Cover</title>
<link rel="stylesheet" href="https://fonts.googleapis.com/css2?family=Josefin+Sans:wght@300;400&display=swap">
<style>
  :root {
    --stage: #1d1d1d;
    --paper: #0b0b0b;
    --red-bright: #e3242b;
    --red-deep: #6e0c10;
    --orange: #c8511f;
    --gold: #f2c21b;
    --gold-deep: #8a4a12;
    --ink-light: #f2f2f2;
    --ink-muted: #9a9a9a;
  }
  * { margin: 0; padding: 0; box-sizing: border-box; }
  html, body {
    width: 1200px; height: 858px; overflow: hidden;
    background: var(--stage);
    font-family: "Josefin Sans", sans-serif;
  }
  .spread {
    position: absolute; left: 100px; top: 69px;
    width: 1000px; height: 720px;
    display: flex;
  }
  .panel {
    position: relative; width: 500px; height: 720px;
    background: var(--paper); overflow: hidden;
  }
  .panel svg { position: absolute; inset: 0; }
  .panel--back { border-right: 1px solid #000; }
  .panel--front {
    background: radial-gradient(circle at 70% 30%, #2a2a2a 0%, var(--paper) 65%);
  }

  .brand { position: absolute; color: var(--ink-light); text-align: center; }
  .brand__name { font-weight: 400; letter-spacing: 1px; line-height: 1; }
  .brand__tagline { color: var(--ink-muted); font-weight: 300; letter-spacing: 3px; }
  .brand__web { font-weight: 400; letter-spacing: 2px; }

  .brand--back { left: 95px; top: 480px; width: 240px; }
  .brand--back .brand__mark {
    width: 10px; height: 10px; background: var(--gold);
    margin: 0 auto 10px;
  }
  .brand--back .brand__name { font-size: 26px; }
  .brand--back .brand__tagline { font-size: 9px; margin-top: 3px; }
  .brand--back .brand__web { font-size: 8px; margin-top: 4px; }

  .address {
    position: absolute; left: 95px; top: 560px; width: 240px;
    text-align: center; color: var(--ink-light);
    font-weight: 300; font-size: 13px; line-height: 1.3;
  }

  .brand--front { left: 180px; top: 262px; width: 300px; }
  .brand--front .brand__name { font-size: 34px; }
  .brand--front .brand__tagline { font-size: 11px; margin-top: 4px; }
  .brand--front .brand__web { font-size: 10px; margin-top: 6px; }
</style>
</head>
<body>
<main class="spread">
  <section class="panel panel--back">
    <svg width="500" height="720" viewBox="0 0 500 720">
      <defs>
        <linearGradient id="band-red" x1="0" y1="0" x2="0.4" y2="1">
          <stop offset="0" stop-color="var(--red-bright)"/>
          <stop offset="1" stop-color="var(--red-deep)"/>
        </linearGradient>
        <linearGradient id="band-gold" x1="0" y1="1" x2="1" y2="0">
          <stop offset="0" stop-color="var(--gold)"/>
          <stop offset="1" stop-color="var(--gold-deep)"/>
        </linearGradient>
      </defs>
      <polygon class="band-red" points="260,0 500,0 500,570 210,610" fill="url(#band-red)"/>
      <polygon class="band-red-shade" points="500,180 500,570 330,595" fill="#000" opacity="0.25"/>
      <polygon class="band-gold" points="190,610 500,560 500,720 200,720" fill="url(#band-gold)"/>
    </svg>
    <div class="brand brand--back">
      <div class="brand__mark"></div>
      <div class="brand__name">REEL HARBOR</div>
      <div class="brand__tagline">PRODUCTION SERVICES</div>
      <div class="brand__web">www.reelharbordubai.com</div>
    </div>
    <address class="address">
      Blgd. Al Nakheel Tower, Off. 204,<br>
      Al Safwa<br>
      Dubai, UAE<br>
      T: +9714 521 7093<br>
      PoBox. 38215
    </address>
  </section>

  <section class="panel panel--front">
    <svg width="500" height="720" viewBox="0 0 500 720">
      <defs>
        <linearGradient id="strip-red" x1="0" y1="0" x2="0" y2="1">
          <stop offset="0" stop-color="var(--red-bright)"/>
          <stop offset="1" stop-color="var(--red-deep)"/>
        </linearGradient>
        <linearGradient id="fold-warm" x1="0" y1="1" x2="1" y2="0">
          <stop offset="0" stop-color="var(--gold)"/>
          <stop offset="0.5" stop-color="var(--orange)"/>
          <stop offset="1" stop-color="var(--red-bright)"/>
        </linearGradient>
      </defs>
      <rect class="illustration-strip" x="0" y="0" width="150" height="560" fill="url(#strip-red)"
            role="img" aria-label="Red film strip running down the panel"/>
      <rect class="illustration-fold" x="70" y="430" width="430" height="290" fill="url(#fold-warm)"
            role="img" aria-label="Folded paper crane in red, orange and gold"/>
    </svg>
    <div class="brand brand--front">
      <div class="brand__name">REEL HARBOR</div>
      <div class="brand__tagline">PRODUCTION SERVICES</div>
      <div class="brand__web">www.reelharbordubai.com</div>
    </div>
  </section>
</main>
</body>
</html>
```